Business Brochure Design Project

BRIGHTWATER FIELD SERVICES
Our company requires a business brochure designed, this design will be printed and emailed to prospective corporate clients to provide an understanding of our businesses services. The written content required in this brochure is attached as a word document.

DESIGN
The design needs to hold your attention and identify the company brand. An A4 portrait format will be used with a white background. Brochure pages will never be viewed side by side as most clients will recieve this as a pdf document attached to an email so considered this in your design. Colour graphics and images will be used to enhance the content and draw people in. To reflect quality, only high resolution images that are clear, sharp and in focus will be used. Please use the CMYK colour model when designing as this brochure will also be printed.

LOOK AND FEEL
The design needs to be savvy, appear uncluttered and have an attitude of a market leader. I want something that stands out in the crowd and effectively markets my businesses brand. It needs to be elegant, modern and have a corporate feel. I want something that has energy, is fresh, innovative, exciting and inviting.

FINISHED PRODUCT
All content in the photo shop design needs to be fully editable including text. Our business has a copy of photo shop CS6, so the finished product must be compatible with this version of software. Each page must contain the text “Copyright © 2013 Brightwater Field Services. All rights reserved”
Updates

Hi all

I will also be setting up a stationay project soon, if your are interested in being part of it please let me know.

Thanks

                          

I like designs that use a white background with the use of red, black and grey colours within

 

To all designers

Thanks for the great design work; I look forward to working with you all again in the future

 

Regards Marcus Henley

Industry/Entity Type

Shop

Requirements
Must have
• This design must be professional and of the highest calibre

Please use the CMYK colour model as this is the formatt by printers.

Business contact details must be clearly visible on the cover page
Should not have
• Each part of my business advertising needs to look interesting in its own right. This insures companies are intrigued to find out more about our services, who we are and what we do. Please do not design something that looks identical to my webpage site or Facebook page. Your design needs to adds value to the overall promotional impact of my business.

The design should not be based off a generic design template, it needs to be unique.

```html
<!DOCTYPE html>
<html lang="en">
<head>
<meta charset="utf-8">
<title>Brightwater Field Services – Testimonials</title>
<link rel="stylesheet" href="https://fonts.googleapis.com/css2?family=Archivo:wght@700;800&family=Arimo:ital,wght@0,400;0,700;1,400&display=swap">
<style>
  :root {
    --brand-red: #e3101b;
    --ink: #1a1a1a;
    --body-ink: #222222;
    --muted: #555555;
    --paper: #ffffff;
    --photo-light: #dfe8f2;
    --photo-mid: #8ea4bd;
    --photo-dark: #2e3d55;
  }
  * { box-sizing: border-box; margin: 0; padding: 0; }
  html, body { width: 848px; height: 1200px; overflow: hidden; background: var(--paper); }
  .page {
    position: relative;
    width: 848px;
    height: 1200px;
    background: var(--paper);
    font-family: "Arimo", Arial, sans-serif;
    color: var(--body-ink);
    overflow: hidden;
  }

  /* Header */
  .header-edge { position: absolute; left: 0; top: 0; width: 45px; height: 152px; background: var(--brand-red); }
  .brand { position: absolute; left: 76px; top: 66px; display: flex; align-items: center; gap: 10px; white-space: nowrap; }
  .brand-dot { width: 34px; height: 34px; border-radius: 50%; background: var(--brand-red); flex: none; }
  .brand-name {
    font-family: "Archivo", Arial, sans-serif;
    font-weight: 800;
    font-size: 19px;
    line-height: 1;
    color: var(--ink);
    letter-spacing: -0.2px;
  }
  .brand-tagline {
    position: absolute; left: 120px; top: 104px;
    font-size: 8.5px; color: var(--muted); white-space: nowrap;
  }
  .header-bar-wide { position: absolute; left: 507px; top: 0; width: 13px; height: 152px; background: var(--brand-red); }
  .header-bar-narrow { position: absolute; left: 527px; top: 0; width: 40px; height: 152px; background: var(--brand-red); }
  .header-photo {
    position: absolute; left: 569px; top: 0; width: 279px; height: 152px;
    background: linear-gradient(120deg, var(--photo-light) 0%, #c4d3e3 40%, var(--photo-mid) 70%, var(--photo-dark) 100%);
  }

  /* Testimonials */
  .testimonial { position: absolute; left: 60px; width: 730px; }
  .testimonial-title {
    font-family: "Archivo", Arial, sans-serif;
    font-weight: 800;
    font-size: 15.5px;
    color: var(--brand-red);
    line-height: 1;
    margin-bottom: 5px;
  }
  .testimonial-quote {
    font-style: italic;
    font-size: 13.9px;
    letter-spacing: -0.25px;
    line-height: 18.8px;
    color: var(--body-ink);
  }
  .testimonial-meta {
    position: relative;
    height: 20px;
    font-weight: 700;
    font-size: 15px;
    color: var(--ink);
    margin-top: 2px;
  }
  .testimonial-meta span { position: absolute; top: 0; }
  .meta-name { left: 0; }
  .meta-title { left: 236px; }
  .meta-project { left: 425px; }

  .t1 { top: 236px; }
  .t2 { top: 462px; }
  .t3 { top: 688px; }
  .t4 { top: 914px; }

  /* Footer */
  .footer-sweep {
    position: absolute; left: 0; top: 1040px; width: 848px; height: 89px;
    background: linear-gradient(180deg, rgba(230,230,230,0) 0%, rgba(225,225,225,0.45) 100%);
  }
  .footer {
    position: absolute; left: 0; top: 1129px; width: 848px; height: 71px;
    background: var(--brand-red);
    color: var(--paper);
    font-weight: 700;
    font-size: 11px;
    text-align: center;
    padding-top: 9px;
  }
</style>
</head>
<body>
<div class="page">
  <header>
    <div class="header-edge"></div>
    <div class="brand">
      <div class="brand-dot"></div>
      <div class="brand-name">BRIGHTWATER FIELD SERVICES</div>
    </div>
    <div class="brand-tagline">Providing Effective Project Controls and Management Solutions</div>
    <div class="header-bar-wide"></div>
    <div class="header-bar-narrow"></div>
    <div class="header-photo" role="img" aria-label="Photo of a smiling business team giving thumbs up in an office"></div>
  </header>

  <main>
    <section class="testimonial t1">
      <h2 class="testimonial-title">TESTIMONIALS 1</h2>
      <p class="testimonial-quote">I had the opportunity to work with Marcus within the Harbourline LNG project in Queensland. He was a pleasure to work with and had skills that in my experience few people possess. He was assertive, proactive and applied himself and his experience to ensure cost and project controls were clear and reporting was on time. He worked very well within the team environment and was always willing to get involved and help in many ways others couldn't. His varied experiences with in the Mining, Oil and Gas industries would be a definite asset to any company looking for an industry provider to provide on time cost and controls schedules. I would definitely recommend him and look forward to working with him again.</p>
      <div class="testimonial-meta"><span class="meta-name">NAME</span><span class="meta-title">TITLE</span><span class="meta-project">PROJECT</span></div>
    </section>

    <section class="testimonial t2">
      <h2 class="testimonial-title">TESTIMONIALS 2</h2>
      <p class="testimonial-quote">I had the opportunity to work with Marcus within the Harbourline LNG project in Queensland. He was a pleasure to work with, and had skills that in my experience few people possess. He was assertive, proactive and applied himself and his experience to ensure cost and project controls were clear and reporting was on time. He worked very well within the team environment and was always willing to get involved and help in many ways others couldn't. His varied experiences with in the Mining, Oil and Gas industries would be a definite asset to any company looking for an industry provider to provide on time cost and controls schedules. I would definitely recommend him and look forward to working with him again.</p>
      <div class="testimonial-meta"><span class="meta-name">NAME</span><span class="meta-title">TITLE</span><span class="meta-project">PROJECT</span></div>
    </section>

    <section class="testimonial t3">
      <h2 class="testimonial-title">TESTIMONIALS 3</h2>
      <p class="testimonial-quote">I had the opportunity to work with Marcus within the Harbourline LNG project in Queensland. He was a pleasure to work with and had skills that in my experience few people possess. He was assertive, proactive and applied himself and his experience to ensure cost and project controls were clear and reporting was on time. He worked very well within the team environment and was always willing to get involved and help in many ways others couldn't. His varied experiences with in the Mining, Oil and Gas industries would be a definite asset to any company looking for an industry provider to provide on time cost and controls schedules. I would definitely recommend him and look forward to working with him again.</p>
      <div class="testimonial-meta"><span class="meta-name">NAME</span><span class="meta-title">TITLE</span><span class="meta-project">PROJECT</span></div>
    </section>

    <section class="testimonial t4">
      <h2 class="testimonial-title">TESTIMONIALS 4</h2>
      <p class="testimonial-quote">I had the opportunity to work with Marcus within the Harbourline LNG project in Queensland. He was a pleasure to work with and had skills that in my experience few people possess. He was assertive, proactive and applied himself and his experience to ensure cost and project controls were clear and reporting was on time. He worked very well within the team environment and was always willing to get involved and help in many ways others couldn't. His varied experiences with in the Mining, Oil and Gas industries would be a definite asset to any company looking for an industry provider to provide on time cost and controls schedules. I would definitely recommend him and look forward to working with him again.</p>
      <div class="testimonial-meta"><span class="meta-name">NAME</span><span class="meta-title">TITLE</span><span class="meta-project">PROJECT</span></div>
    </section>
  </main>

  <div class="footer-sweep" role="img" aria-label="Faint grey sweeping line pattern above the footer"></div>
  <footer class="footer">Copyright © 2013 Brightwater Field Services. All rights reserved</footer>
</div>
</body>
</html>
```